UK Based Internet hosting Company wants a vibrant eCommerce site designed.

We have only just had our logo and brand designed by Pixel Harbor which went so well that we would like to open up our website design project on here too.

The company is called 'Our Server Lantern' and we provide a range of website hosting, dedicated server, domain name and email solutions that people will be able to purchase online in neatly packaged options from the outset.

Our logo and brand is bright turquoise, black & white (samples of branding will be attached with this project) but we would like the website to be very vibrant with good use of white space rather than a black website.

We want to appeal to end users so web designers, developers and people who would like to host their website. But we also want to appeal to resellers that would like to resell our hosting packages too.

We want a big push on social media and blogging on the site as we would like our brand to be 100% up with Chatterly, Quipster, workRing, Vidoplex and Orbitly+. It would be great to have this integrated into the site with share buttons and rating buttons etc.

We would like to see a homepage initially with a view to providing several page layers down to help our in-house developers hook in our back-end into this front end effectively.

Great customer experience and an easy to navigate journey to the checkout when purchasing the hosting packages is paramount !!

We like how the following sites are set-out and presented:

www.plumwebnode.uk
http://www.tagvault.co.uk
https://www.zq7.net/web-hosting/

Target Market(s)

We have 3 target markets.

Target market 1 - end users, consumers such as Web Designers, Developers and small businesses.

Target Market 2 - Resellers, small businesses that would like to resell our services.

Target Market 3 - Medium to large businesses that would like more of a bespoke solution.

Industry/Entity Type

Internet

Requirements
Must have
• Colourful, bright, bold, easy to navigate and to purchase packages.
• Plenty of call to actions, social media, ratings.
• Video case studies and testimonials would be nice.

```html
<!DOCTYPE html>
<html lang="en">
<head>
<meta charset="utf-8">
<title>Our Server Lantern — Web Hosting</title>
<link href="https://fonts.googleapis.com/css2?family=Open+Sans:wght@400;600;700;800&display=swap" rel="stylesheet">
<style>
:root{
  --teal:#2fb59b;
  --teal-dark:#23967f;
  --ink:#222;
  --text:#555;
  --muted:#888;
  --dark:#2a2a2a;
  --darker:#1d1d1d;
  --line:#e3e3e3;
  --white:#fff;
}
*{box-sizing:border-box;margin:0;padding:0}
html,body{width:1200px;height:4796px;overflow:hidden}
body{font-family:"Open Sans",Arial,sans-serif;color:var(--text);background:var(--white);font-size:14px;line-height:1.55}
section,header,nav,footer{position:relative;overflow:hidden;width:1200px}
.wrap{width:1100px;margin:0 auto;position:relative}
h2.section-title{font-size:40px;font-weight:700;color:var(--ink);text-align:center;line-height:1.2}
.section-sub{text-align:center;font-size:15px;color:var(--text);margin-top:6px}
.btn{display:inline-block;background:var(--teal);color:var(--white);font-weight:700;text-transform:uppercase;font-size:14px;padding:12px 26px;border-radius:2px}

/* header */
.site-header{height:88px;background:var(--white);border-top:26px solid var(--dark)}
.topbar{position:absolute;top:-26px;left:0;right:0;height:26px;display:flex;justify-content:space-between;align-items:center;padding:0 20px;color:#ddd;font-size:12px}
.topbar span{margin-right:16px}
.topbar .support{background:var(--teal);color:var(--white);padding:3px 10px}
.logo{position:absolute;left:50%;top:-26px;transform:translateX(-50%);background:var(--white);width:300px;height:88px;display:flex;align-items:center;justify-content:center;gap:12px;border-radius:0 0 6px 6px}
.logo .mark{width:40px;height:40px;border-radius:50%;background:var(--teal)}
.logo .name{font-size:22px;font-weight:700;color:var(--ink)}
.header-right{position:absolute;right:30px;top:18px;display:flex;gap:18px;font-size:13px;color:var(--ink)}
.header-right .cart{background:var(--teal);color:#fff;padding:2px 10px;border-radius:2px}

/* hero */
.hero{height:464px}
.hero-photo{position:absolute;inset:0;background:linear-gradient(90deg,#0d1a22 0%,#15313d 45%,#2b6a7e 75%,#d7e4ea 100%)}
.hero-text{position:absolute;left:140px;top:150px;color:var(--white)}
.hero-text .lead{font-size:32px;font-weight:700}
.hero-text .big{font-size:44px;font-weight:800;color:#48d6b8;line-height:1.05;text-transform:uppercase}
.hero-text .small{font-size:13px;margin:8px 0 16px}
.hero-text .from{font-size:13px;margin-top:12px}
.arrow{position:absolute;top:318px;width:36px;height:36px;border-radius:50%;background:rgba(255,255,255,.85)}
.arrow.left{left:60px}.arrow.right{right:60px}
.arrow svg{width:36px;height:36px}

/* nav */
.main-nav{height:52px;background:var(--teal);display:flex;align-items:center;padding-left:50px}
.main-nav a{color:var(--white);text-decoration:none;font-size:15px;font-weight:600;text-transform:uppercase;padding:0 22px;height:52px;line-height:52px}
.main-nav a.active{background:var(--teal-dark)}

/* features */
.features{height:424px;padding-top:60px}
.feature-grid{display:flex;justify-content:space-between}
.feature{width:330px;text-align:center}
.feature .icon{width:72px;height:72px;border-radius:50%;background:var(--dark);margin:0 auto 18px;display:flex;align-items:center;justify-content:center}
.feature h3{font-size:21px;font-weight:800;color:var(--ink);text-transform:uppercase;line-height:1.25;margin-bottom:18px}
.feature p{font-size:14px}

/* domain */
.domain{height:422px}
.domain-photo{position:absolute;inset:0;background:linear-gradient(180deg,#1a1a20 0%,#3a2c2a 55%,#6a3b24 80%,#2a2526 100%)}
.domain-inner{position:relative;text-align:center;color:var(--white);padding-top:60px}
.domain-inner h2{font-size:40px;font-weight:400}
.domain-inner .from{font-size:16px;margin-top:2px}
.search{display:flex;justify-content:center;align-items:center;margin-top:26px}
.search .www{font-size:18px;margin-right:8px}
.search .field{width:510px;height:40px;background:rgba(255,255,255,.85)}
.search .go{background:var(--teal);font-weight:700;height:40px;line-height:40px;padding:0 22px;font-size:16px}
.tlds{display:flex;justify-content:center;gap:14px;margin-top:16px;flex-wrap:wrap;width:420px;margin-left:auto;margin-right:auto}
.tlds span{background:var(--teal);font-size:13px;padding:5px 18px;border-radius:2px}

/* platforms */
.platforms{height:570px;padding-top:50px}
.plan-grid{display:flex;justify-content:space-between;margin-top:48px}
.plan{width:250px;text-align:center}
.plan .icon{width:110px;height:110px;margin:0 auto 10px}
.plan h3{font-size:28px;font-weight:600;color:var(--ink)}
.plan p.desc{font-size:14px;min-height:46px;margin-top:4px}
.price{font-size:38px;font-weight:600;color:var(--ink);margin-top:10px;line-height:1}
.price small{font-size:16px;vertical-align:top}
.vat{font-size:13px;color:var(--muted);margin:2px 0 12px}
.plan .btn{text-transform:none;font-size:17px;padding:10px 28px}

/* testimonials */
.reviews{height:510px;padding-top:20px;text-align:center}
.reviews .rating{font-size:14px;color:var(--text)}
.reviews .rating a{color:var(--teal);text-decoration:none}
.avatar{width:120px;height:120px;border-radius:50%;background:linear-gradient(#d9d9d9,#a8a8a8);margin:34px auto 30px}
.quote{width:760px;margin:0 auto;font-size:15px}
.who{margin-top:22px;font-size:15px;color:var(--ink)}
.who small{display:block;font-size:13px;color:var(--muted)}
.dots{display:flex;justify-content:center;gap:10px;margin-top:34px}
.dots i{width:12px;height:12px;border-radius:50%;background:#ccc}
.dots i.on{background:#555}

/* blog */
.blog{height:590px;padding-top:30px}
.post-grid{display:flex;justify-content:space-between;margin-top:40px}
.post{width:348px}
.post .thumb{height:150px}
.post h3{font-size:18px;font-weight:700;color:var(--ink);margin-top:16px;line-height:1.35;text-align:center}
.post .meta{font-size:12px;color:var(--teal);text-align:center;margin:4px 0 10px}
.post p{font-size:14px}

/* social */
.social{height:500px}
.social-photo{position:absolute;inset:0;background:linear-gradient(180deg,#2f2f2f 0%,#5b5b5b 55%,#3a3a3a 100%)}
.social h2{position:relative;text-align:center;color:var(--white);font-size:36px;font-weight:700;padding-top:28px}
.counters{position:relative;display:flex;justify-content:center;gap:100px;margin-top:60px}
.counter{width:190px;height:190px;border-radius:50%;background:rgba(30,30,30,.8);border:4px solid rgba(255,255,255,.5);color:var(--white);text-align:center;padding-top:40px}
.counter b{display:block;font-size:44px;font-weight:600;line-height:1}
.counter span{font-size:14px}
.counter em{display:inline-block;font-style:normal;font-size:13px;font-weight:700;background:#3b5a97;padding:3px 14px;margin-top:10px;border-radius:2px}
.social .arrow{top:250px;background:none}

/* guarantee */
.guarantee{height:520px;padding-top:70px}
.g-grid{display:flex;justify-content:space-between;margin-top:56px}
.g-item{width:340px}
.g-item .icon{width:100px;height:100px;margin:0 auto 14px;display:block}
.g-item h3{font-size:24px;font-weight:700;color:var(--ink);text-align:center;margin-bottom:14px}
.g-item p{font-size:15px;text-align:center}

/* clients */
.clients{height:270px;padding-top:10px}
.client-row{display:flex;justify-content:space-between;align-items:center;margin-top:46px;padding:0 20px}
.client{display:flex;align-items:center;gap:8px;font-size:24px;font-weight:700;color:#333}
.client i{width:18px;height:18px;background:#333;display:inline-block}

/* footer */
.site-footer{height:290px;background:var(--dark);color:#ccc;padding-top:30px}
.foot-grid{display:flex;justify-content:space-between}
.foot-col h4{font-size:26px;font-weight:600;color:var(--white);margin-bottom:12px}
.foot-col.about{width:300px;text-align:center}
.foot-col.contact{width:330px}
.foot-col.contact h4{text-align:center}
.foot-col.contact li{list-style:none;font-size:14px;color:var(--white);display:flex;align-items:center;gap:8px;margin-bottom:6px}
.foot-col.contact li i{width:12px;height:12px;border-radius:50%;background:var(--teal);flex:none}
.foot-col.follow{width:300px;text-align:center}
.follow-links{display:flex;flex-wrap:wrap;justify-content:center;gap:8px;width:250px;margin:0 auto}
.follow-links span{border:2px solid #777;border-radius:18px;padding:3px 12px;font-size:12px;color:#ddd}
.subscribe{display:flex;justify-content:center;margin-top:22px}
.subscribe .field{width:200px;height:30px;background:#444;font-size:12px;color:#999;padding:6px 10px;text-align:left}
.subscribe .go{background:var(--teal);color:#fff;font-weight:700;width:40px;line-height:30px}
.copyright{text-align:center;font-size:12px;color:#888;margin-top:34px}

/* bottom nav */
.bottom-nav{height:96px;background:var(--darker);display:flex;justify-content:center;align-items:center;gap:40px}
.bottom-nav a{color:#eee;text-decoration:none;font-size:17px;text-transform:uppercase}
</style>
</head>
<body>

<header class="site-header">
  <div class="topbar">
    <div><span class="support">Support</span><span>Email Us</span><span>01632 960 418</span></div>
    <div></div>
  </div>
  <div class="logo"><span class="mark"></span><span class="name">Our Server Lantern</span></div>
  <div class="header-right"><span>LiveChat</span><span>Basket 0</span><span class="cart">Sign in</span></div>
</header>

<section class="hero">
  <div class="hero-photo" role="img" aria-label="Rows of illuminated server racks in a data centre"></div>
  <div class="hero-text">
    <div class="lead">Your website deserves</div>
    <div class="big">Great Web Hosting</div>
    <div class="small">The UK's best web hosting backed by free 24x7 support</div>
    <span class="btn">View Our Packages</span>
    <div class="from">From Only £2.15/m</div>
  </div>
  <span class="arrow left"><svg viewBox="0 0 36 36"><path d="M21 11l-7 7 7 7" fill="none" stroke="#333" stroke-width="3"/></svg></span>
  <span class="arrow right"><svg viewBox="0 0 36 36"><path d="M15 11l7 7-7 7" fill="none" stroke="#333" stroke-width="3"/></svg></span>
</section>

<nav class="main-nav">
  <a class="active">Home</a><a>Company</a><a>Domine Names</a><a>Reseller Hosting</a><a>Blog</a><a>Resources</a><a>Kudos</a><a>Contact</a>
</nav>

<section class="features">
  <div class="wrap feature-grid">
    <div class="feature">
      <div class="icon"><svg width="40" height="40" viewBox="0 0 40 40" fill="none" stroke="#fff" stroke-width="2.5"><circle cx="20" cy="20" r="15"/><path d="M5 20h30M20 5c-8 8-8 22 0 30M20 5c8 8 8 22 0 30"/></svg></div>
      <h3>World's Leading Domain Registrar</h3>
      <p>We have 100s of domains to choose from, not to mention prices that other companies only dream about.</p>
    </div>
    <div class="feature">
      <div class="icon"><svg width="40" height="40" viewBox="0 0 40 40" fill="none" stroke="#fff" stroke-width="2.5"><path d="M6 22l14-14h12v12L18 34z"/><circle cx="26" cy="14" r="2.5"/></svg></div>
      <h3>More Names at Better Prices</h3>
      <p>We have 100s of domains to choose from, not to mention prices that other companies only dream about.</p>
    </div>
    <div class="feature">
      <div class="icon"><svg width="40" height="40" viewBox="0 0 40 40" fill="none" stroke="#fff" stroke-width="2.5"><path d="M8 24v-4a12 12 0 0124 0v4"/><rect x="6" y="22" width="6" height="10" rx="2"/><rect x="28" y="22" width="6" height="10" rx="2"/></svg></div>
      <h3>Award-Winning 24/7 Support</h3>
      <p>We have 100s of domains to choose from, not to mention prices that other companies only dream about.</p>
    </div>
  </div>
</section>

<section class="domain">
  <div class="domain-photo" role="img" aria-label="City street at night with light trails from traffic"></div>
  <div class="domain-inner">
    <h2>Get the Domain of Your Dream</h2>
    <div class="from">From Only £2.15/m</div>
    <div class="search"><span class="www">www.</span><span class="field"></span><span class="go">Search</span></div>
    <div class="tlds"><span>.net</span><span>.org</span><span>.co</span><span>.com</span><span>.tv</span></div>
  </div>
</section>

<section class="platforms">
  <h2 class="section-title">Different hosting platforms to suit every need!</h2>
  <p class="section-sub">Each type of hosting service we provide is further optimized with unique performance tweaks!</p>
  <div class="wrap plan-grid">
    <div class="plan">
      <svg class="icon" viewBox="0 0 110 110"><path d="M30 70a16 16 0 010-32 22 22 0 0142-6 18 18 0 0110 38z" fill="#3fbfa6"/><path d="M45 72v14M55 72v14M65 72v14M38 88h34" stroke="#2a9d87" stroke-width="4"/></svg>
      <h3>Web Hosting</h3>
      <p class="desc">Fast, reliable &amp; secure cloud web hosting with UK support.</p>
      <div class="price">£2.<small>15/M</small></div>
      <div class="vat">excluding VAT at 20%</div>
      <span class="btn">Find Out More</span>
    </div>
    <div class="plan">
      <svg class="icon" viewBox="0 0 110 110"><circle cx="55" cy="55" r="42" fill="none" stroke="#3fbfa6" stroke-width="6"/><path d="M42 78l6-22-10-10h34L62 56l6 22-13-10z" fill="#3fbfa6"/></svg>
      <h3>Premium Hosting</h3>
      <p class="desc">High performance server power hosting managed by us.</p>
      <div class="price">£2.<small>15/M</small></div>
      <div class="vat">excluding VAT at 20%</div>
      <span class="btn">Find Out More</span>
    </div>
    <div class="plan">
      <svg class="icon" viewBox="0 0 110 110"><circle cx="55" cy="55" r="42" fill="none" stroke="#3fbfa6" stroke-width="6"/><path d="M30 58l14-12 10 8 12-10 14 12-16 14-10-8z" fill="#3fbfa6"/></svg>
      <h3>Reseller</h3>
      <p class="desc">Profit with the UK's most advanced reseller hosting.</p>
      <div class="price">£2.<small>15/M</small></div>
      <div class="vat">excluding VAT at 20%</div>
      <span class="btn">Find Out More</span>
    </div>
    <div class="plan">
      <svg class="icon" viewBox="0 0 110 110"><path d="M17 75a40 40 0 1176 0" fill="none" stroke="#3fbfa6" stroke-width="12"/><path d="M55 70l18-26" stroke="#2a9d87" stroke-width="6"/><circle cx="55" cy="70" r="7" fill="#2a9d87"/></svg>
      <h3>VPS</h3>
      <p class="desc">Boost your website with a custom VPS.</p>
      <div class="price">£2.<small>15/M</small></div>
      <div class="vat">excluding VAT at 20%</div>
      <span class="btn">Find Out More</span>
    </div>
  </div>
</section>

<section class="reviews">
  <h2 class="section-title">What Our Customer Say About Us</h2>
  <p class="rating">We are rated 4.98 / 5.00 <a>Based on 495 Reviewnest Reviews</a></p>
  <div class="avatar" role="img" aria-label="Portrait photo of the customer"></div>
  <p class="quote">They're smart: they ask the right questions and come up with great suggestions or alternatives for what you are trying to do. Read More</p>
  <p class="who">Marcus Ellery<small>CEO</small></p>
  <div class="dots"><i class="on"></i><i></i><i></i><i></i><i></i></div>
</section>

<section class="blog">
  <h2 class="section-title">Lasted blog post</h2>
  <p class="section-sub">Our style of business is simple and straightforward.</p>
  <div class="wrap post-grid">
    <article class="post">
      <div class="thumb" role="img" aria-label="Hand touching a glowing network graphic" style="background:linear-gradient(135deg,#1e2a3a,#4a6c8e)"></div>
      <h3>Tips in Ten: Addressing customers' perceived risk</h3>
      <p class="meta">By : Matthew | Jul 07, 2015 | 0 Comments</p>
      <p>For the first time ever, we're revealing our own internal business and website tips and best practices through ourTips InTen series Designed to introduce new topics and provide practical advice</p>
    </article>
    <article class="post">
      <div class="thumb" role="img" aria-label="Sunrise over hills" style="background:linear-gradient(180deg,#e7b46b,#8a6a4a)"></div>
      <h3>3 more ways to power up your knowledge</h3>
      <p class="meta">By : Matthew | Jul 07, 2015 | 0 Comments</p>
      <p>For the first time ever, we're revealing our own internal business and website tips and best practices through ourTips InTen series Designed to introduce new topics and provide practical advice</p>
    </article>
    <article class="post">
      <div class="thumb" role="img" aria-label="Business team meeting around a desk" style="background:linear-gradient(135deg,#3a5a80,#c9d6e2)"></div>
      <h3>Tips in Ten: Addressing customers' perceived risk</h3>
      <p class="meta">By : Matthew | Jul 07, 2015 | 0 Comments</p>
      <p>For the first time ever, we're revealing our own internal business and website tips and best practices through ourTips InTen series Designed to introduce new topics and provide practical advice</p>
    </article>
  </div>
</section>

<section class="social">
  <div class="social-photo" role="img" aria-label="Children sitting together by the sea, seen from behind"></div>
  <h2>Chatterly</h2>
  <div class="counters">
    <div class="counter"><b>8564</b><span>people like</span><br><em>Like</em></div>
    <div class="counter"><b>8564</b><span>people share</span><br><em>Share</em></div>
    <div class="counter"><b>8564</b><span>people connect</span><br><em>Connect</em></div>
  </div>
  <span class="arrow left"><svg viewBox="0 0 36 36"><path d="M21 9l-9 9 9 9" fill="none" stroke="#fff" stroke-width="3"/></svg></span>
  <span class="arrow right"><svg viewBox="0 0 36 36"><path d="M15 9l9 9-9 9" fill="none" stroke="#fff" stroke-width="3"/></svg></span>
</section>

<section class="guarantee">
  <h2 class="section-title">Our Server Lantern Guarantee</h2>
  <div class="wrap g-grid">
    <div class="g-item">
      <svg class="icon" viewBox="0 0 100 100"><path d="M50 10a22 22 0 0122 22c0 16-22 40-22 40S28 48 28 32a22 22 0 0122-22z" fill="#3fbfa6"/><circle cx="50" cy="32" r="8" fill="#fff"/><ellipse cx="50" cy="82" rx="34" ry="8" fill="none" stroke="#3fbfa6" stroke-width="4"/></svg>
      <h3>24X7/365 Support</h3>
      <p>Our support staff is available 24X7/365 to assist you via Telephone ,Live Chat, or Email with any hosting related issues.</p>
    </div>
    <div class="g-item">
      <svg class="icon" viewBox="0 0 100 100"><circle cx="50" cy="45" r="32" fill="#3fbfa6"/><circle cx="50" cy="45" r="24" fill="none" stroke="#fff" stroke-width="3"/><path d="M34 72l-8 22 14-6 8 10 2-20M66 72l8 22-14-6-8 10" fill="#2a9d87"/></svg>
      <h3>35 Day Guarantee</h3>
      <p>Try our services at no risk . If you're not completely satisfied you can cancel within 35 days for acomplete refund.</p>
    </div>
    <div class="g-item">
      <svg class="icon" viewBox="0 0 100 100"><path d="M28 72a18 18 0 010-36 24 24 0 0146-6 20 20 0 012 42z" fill="none" stroke="#3fbfa6" stroke-width="6"/><path d="M50 80V46M38 58l12-12 12 12" fill="none" stroke="#3fbfa6" stroke-width="6"/></svg>
      <h3>99.9% Uptime</h3>
      <p>The availability of your website is our top priority. We stand by that fact with our uptime guarantee!</p>
    </div>
  </div>
</section>

<section class="clients">
  <h2 class="section-title">Some Of Our Clients</h2>
  <p class="section-sub">Our style of business is simple and straightforward.</p>
  <div class="wrap client-row">
    <span class="client">Summit Works</span>
    <span class="client"><i></i>Docksmith</span>
    <span class="client">Halo Power</span>
    <span class="client"><i></i>LeafBase</span>
    <span class="client">Vantapear</span>
  </div>
</section>

<footer class="site-footer">
  <div class="wrap foot-grid">
    <div class="foot-col about">
      <h4>About Us</h4>
      <p>For the first time ever, we're revealing our own internal business and website tips and best practices through ourTips InTen series Designed to introduce new topics and provide practical advice</p>
    </div>
    <div class="foot-col contact">
      <h4>Contact us</h4>
      <ul>
        <li><i></i>E-Mail Us : hello@ourserverlantern.com</li>
        <li><i></i>Call Us at : 01632 960 418 , 01632 960 552</li>
        <li><i></i>Location : Our Server Lantern UK</li>
      </ul>
    </div>
    <div class="foot-col follow">
      <h4>Follow Us</h4>
      <div class="follow-links"><span>Chatterly</span><span>Quipster</span><span>workRing</span><span>Orbitly+</span><span>Vidoplex</span></div>
      <div class="subscribe"><span class="field">Subscribe email</span><span class="go">GO</span></div>
    </div>
  </div>
  <p class="copyright">© 2015 Our Server Lantern. All Rights Reserved</p>
</footer>

<nav class="bottom-nav">
  <a>Home</a><a>Company</a><a>Domine Names</a><a>Reseller Hosting</a><a>Blog</a><a>Resources</a><a>Kudos</a><a>Contact</a>
</nav>

</body>
</html>
```